Cover for Where the Lantern Drifts Beyond the Quiet Shore

Cover for a book that describes everything that happens to a person, from pre-birth life plans through growing in compassion and wisdom to death and living in the afterlife. The information is revealed in messages from people living in the life after this life. The title is Patterns Behind the Seasons of Your Journey and Beyond: Told by Voices Dwelling Past the Veil. Author is T. Milton Baxby. Book size is 6 by 9.

Target Market(s)

General

Font styles to use
Serif

```html
<!DOCTYPE html>
<html lang="en">
<head>
<meta charset="utf-8">
<title>Patterns Behind the Seasons of Your Journey and Beyond</title>
<link rel="stylesheet" href="https://fonts.googleapis.com/css2?family=Tinos:wght@400;700&display=swap">
<style>
  :root {
    --title-red: #c1232b;
    --ink: #141210;
    --stone-light: #f3efe2;
    --stone-mid: #d9d2bd;
    --stone-sage: #c9cfbd;
    --earth: #b89a78;
    --earth-dark: #8f7358;
    --glow: #fffbea;
  }
  html, body {
    margin: 0;
    padding: 0;
    width: 800px;
    height: 1200px;
    overflow: hidden;
    background: #ffffff;
  }
  .cover {
    position: relative;
    width: 800px;
    height: 1200px;
    overflow: hidden;
    font-family: "Tinos", "Times New Roman", serif;
  }
  .cover-art {
    position: absolute;
    inset: 0;
    background:
      radial-gradient(ellipse 200px 260px at 300px 880px, var(--glow) 0%, rgba(255,248,225,0.85) 35%, rgba(255,248,225,0) 100%),
      radial-gradient(ellipse 420px 300px at 600px 420px, rgba(250,247,236,0.9) 0%, rgba(250,247,236,0) 100%),
      linear-gradient(180deg, var(--stone-sage) 0%, var(--stone-light) 30%, var(--stone-mid) 62%, var(--earth) 88%, var(--earth-dark) 100%);
  }
  .title {
    margin: 0;
    font-weight: 700;
    color: var(--title-red);
  }
  .title-line {
    position: absolute;
    left: 0;
    width: 800px;
    text-align: center;
    line-height: 1;
  }
  .title-line--major { font-size: 62px; font-weight: 700; letter-spacing: -0.5px; }
  .title-line--minor { font-size: 42px; font-weight: 400; }
  .subtitle {
    position: absolute;
    left: 0;
    width: 800px;
    top: 638px;
    margin: 0;
    text-align: center;
    font-size: 28px;
    font-weight: 400;
    color: var(--ink);
    letter-spacing: 0.3px;
  }
  .author {
    position: absolute;
    left: 0;
    width: 800px;
    top: 1042px;
    margin: 0;
    text-align: center;
    font-size: 72px;
    font-weight: 400;
    color: var(--ink);
  }
</style>
</head>
<body>
  <main class="cover">
    <div class="cover-art" role="img" aria-label="Photograph of an open stone tomb with a glowing doorway and a round rolled-away stone on dusty ground"></div>
    <h1 class="title">
      <span class="title-line title-line--major" style="top:46px">Patterns</span>
      <span class="title-line title-line--minor" style="top:145px">behind</span>
      <span class="title-line title-line--major" style="top:214px">the Seasons</span>
      <span class="title-line title-line--minor" style="top:314px">of</span>
      <span class="title-line title-line--major" style="top:383px">Your Journey</span>
      <span class="title-line title-line--minor" style="top:482px">and</span>
      <span class="title-line title-line--major" style="top:550px">Beyond</span>
    </h1>
    <p class="subtitle">Told by Voices Dwelling Past the Veil</p>
    <p class="author">T. Milton Baxby</p>
  </main>
</body>
</html>
```